I have a transportation trucking company and I’m expanding and hiring drivers

I need a flyer for my social media to let people know I’m hiring and looking for drivers , Please incorporate my company logo and i need to flyer to give some information about the position, I will upload some examples,

I do need it to say We are hiring!
We are looking for CDL- Class A Drivers
2 Years Minimum Driving Experience
Percentage Pay
Clean Driving Record
No Violations or accidents
Weekly Direct Deposit
Sign On bonus
Holiday Bonus
Detention/ Layover Pay
Must Stay out a minimum of 2 full weeks

Interested in more information?
Email info@maplecresthaul.com
(555) 218-6093

Maplecrest Haul LLC
824 Linden Ferry Lane Suite 200 Jenkintown PA 19000

Industry/Entity Type

Long Distance Trucking

Font styles to use
Serif
Sans Serif
Decorative
Script

Requirements
Must have
• Please incorporate my logo into the flyer

Please have just the flyer take up the whole canvas this will be printed and posted on our social media’s
Nice to have

```html
<!DOCTYPE html>
<html lang="en">
<head>
<meta charset="utf-8">
<title>Maplecrest Haul LLC – Drivers Wanted</title>
<link rel="stylesheet" href="https://fonts.googleapis.com/css2?family=Montserrat:wght@400;500;700;800;900&display=swap">
<style>
  :root {
    --brand-blue: #2f6db5;
    --ink-grey: #585858;
    --star-grey: #4a4a4a;
    --paper: #ffffff;
    --hero-light: #f4f6f8;
    --hero-mid: #c9d2da;
    --hero-truck: #7fb7d6;
  }
  * { box-sizing: border-box; margin: 0; padding: 0; }
  html, body { width: 846px; height: 1200px; overflow: hidden; background: var(--paper); }
  .flyer {
    position: relative;
    width: 846px;
    height: 1200px;
    overflow: hidden;
    background: var(--paper);
    font-family: "Montserrat", Arial, sans-serif;
  }
  .headline {
    position: absolute;
    top: 22px; left: 0; width: 100%;
    text-align: center;
    font-size: 74px;
    font-weight: 900;
    color: var(--brand-blue);
    letter-spacing: 0.5px;
  }
  .hero-art {
    position: absolute;
    top: 112px; left: 0;
    width: 846px; height: 430px;
    background:
      radial-gradient(ellipse 45% 40% at 68% 55%, var(--hero-truck) 0%, rgba(127,183,214,0) 100%),
      radial-gradient(ellipse 40% 35% at 30% 40%, var(--hero-mid) 0%, rgba(201,210,218,0) 100%),
      linear-gradient(180deg, var(--hero-light) 0%, var(--paper) 100%);
  }
  .position-title {
    position: absolute;
    top: 528px; left: 0; width: 100%;
    text-align: center;
    font-size: 52px;
    font-weight: 800;
    line-height: 66px;
    color: var(--ink-grey);
  }
  .benefits {
    position: absolute;
    top: 696px; left: 34px;
    list-style: none;
    font-size: 26px;
    font-weight: 500;
    color: var(--brand-blue);
    line-height: 43px;
  }
  .benefits li { position: relative; padding-left: 36px; }
  .benefits li::before {
    content: "★";
    position: absolute; left: 0; top: 0;
    color: var(--star-grey);
    font-size: 24px;
  }
  .experience-badge {
    position: absolute;
    top: 676px; left: 488px;
    width: 172px; height: 172px;
  }
  .experience-badge svg { position: absolute; inset: 0; }
  .experience-badge .badge-text {
    position: absolute; inset: 0;
    display: flex; align-items: center; justify-content: center;
    text-align: center;
    transform: rotate(-15deg);
    color: var(--paper);
    font-weight: 700;
    font-size: 20px;
    line-height: 24px;
  }
  .company-mark {
    position: absolute;
    top: 880px; left: 516px;
    width: 280px;
    text-align: center;
  }
  .company-mark .mark-square {
    display: block;
    width: 78px; height: 78px;
    margin: 0 auto 18px;
    background: var(--brand-blue);
  }
  .company-mark .mark-name {
    font-size: 30px;
    font-weight: 800;
    color: var(--brand-blue);
    line-height: 34px;
    letter-spacing: 1px;
    text-transform: uppercase;
  }
  .company-address {
    position: absolute;
    top: 1058px; left: 500px;
    width: 312px;
    text-align: center;
    font-size: 19px;
    line-height: 24px;
    color: var(--ink-grey);
  }
  .company-address .legal-name { font-weight: 700; color: var(--brand-blue); }
  .contact-bar {
    position: absolute;
    left: 0; bottom: 0;
    width: 846px; height: 60px;
    background: var(--brand-blue);
    color: var(--paper);
    display: flex; align-items: center; justify-content: center;
    font-size: 24px;
    font-weight: 700;
  }
  .contact-bar .divider { margin: 0 18px; }
</style>
</head>
<body>
<main class="flyer">
  <h1 class="headline">We are hiring!</h1>

  <div class="hero-art" role="img" aria-label="Blue semi truck beside large 3D lettering reading Drivers Needed"></div>

  <h2 class="position-title">We are looking for<br>CDL- Class A Drivers</h2>

  <ul class="benefits">
    <li>Percentage Pay</li>
    <li>Clean Driving Record</li>
    <li>No Violations or accidents</li>
    <li>Weekly Direct Deposit</li>
    <li>Sign On bonus</li>
    <li>Holiday Bonus</li>
    <li>Detention/ Layover Pay</li>
    <li>Must Stay out a minimum<br>of 2 full weeks</li>
  </ul>

  <div class="experience-badge">
    <svg viewBox="0 0 172 172" width="172" height="172" aria-hidden="true">
      <g fill="var(--brand-blue)">
        <rect x="23" y="23" width="126" height="126" transform="rotate(0 86 86)"/>
        <rect x="23" y="23" width="126" height="126" transform="rotate(15 86 86)"/>
        <rect x="23" y="23" width="126" height="126" transform="rotate(30 86 86)"/>
        <rect x="23" y="23" width="126" height="126" transform="rotate(45 86 86)"/>
        <rect x="23" y="23" width="126" height="126" transform="rotate(60 86 86)"/>
        <rect x="23" y="23" width="126" height="126" transform="rotate(75 86 86)"/>
      </g>
    </svg>
    <p class="badge-text">2 Years<br>Minimum<br>Driving<br>Experience</p>
  </div>

  <div class="company-mark">
    <span class="mark-square" aria-hidden="true"></span>
    <p class="mark-name">Maplecrest Haul</p>
  </div>

  <address class="company-address" style="font-style:normal">
    <span class="legal-name">Maplecrest Haul LLC</span><br>
    824 Linden Ferry Lane Suite<br>
    200 Jenkintown PA 19000
  </address>

  <footer class="contact-bar">
    <span>Email: info@maplecresthaul.com</span>
    <span class="divider">|</span>
    <span>(555) 218-6093</span>
  </footer>
</main>
</body>
</html>
```